Business Card Design for Technology Company

New business card design needed for technology company director.
Ideally, the design will fit the style and nature of the industry. We are a supplier of quality products and services, and we hope the design will give customers and suppliers this impression.

Target Market(s)

3D Printing Industry

Industry/Entity Type

Technology Equipment

Contact Information for Business Card

Name: Marcus Lyle
Title: Director
Company address: Factory K4, 7B Morland Road, Springvale Victoria Australia 3150
Telephone: +61-3-8555 6413
Email: marcus.lyle@veranox.com.au
Website: www.veranox.com.au

Requirements
Must have
• All information in business card details
• Company logo
• '3D Printers and 3D Print Filaments' at proper place
Nice to have
• Style to fit the industry
• Colour to fit logo

```html
<!DOCTYPE html>
<html lang="en">
<head>
<meta charset="utf-8">
<title>Veranox – Business Card</title>
<link rel="stylesheet" href="https://fonts.googleapis.com/css2?family=Open+Sans:wght@400;600&display=swap">
<style>
  :root {
    --backdrop: #1c1c1d;
    --card: #222223;
    --ink-emboss: #141415;
    --text-grey: #6f6f72;
    --name-grey: #5c5c60;
    --tagline-grey: #4a4a4d;
    --accent-orange: #f7931e;
    --accent-blue: #1e9bdc;
  }
  * { margin: 0; padding: 0; box-sizing: border-box; }
  html, body { width: 1200px; height: 900px; overflow: hidden; }
  body {
    background: var(--backdrop);
    font-family: "Open Sans", sans-serif;
    position: relative;
  }
  .card {
    position: absolute;
    left: 270px;
    width: 660px;
    height: 377px;
    background: var(--card);
  }
  .card--front { top: 52px; }
  .card--back { top: 471px; }

  /* Front */
  .front-brand {
    position: absolute;
    left: 0; right: 0; top: 100px;
    display: flex; flex-direction: column; align-items: center; gap: 20px;
  }
  .brand-mark {
    width: 92px; height: 92px;
    background: var(--accent-orange);
    flex: none;
  }
  .brand-text { display: flex; flex-direction: column; align-items: center; }
  .brand-name {
    font-weight: 600;
    font-size: 44px;
    line-height: 1.1;
    letter-spacing: 10px;
    margin-right: -10px;
    color: var(--ink-emboss);
    text-transform: uppercase;
  }
  .brand-tagline {
    margin-top: 6px;
    font-size: 12px;
    font-weight: 600;
    letter-spacing: 3px;
    color: var(--tagline-grey);
    text-transform: uppercase;
    white-space: nowrap;
  }

  /* Back */
  .back-brand {
    position: absolute; left: 100px; top: 38px;
    display: flex; align-items: center; gap: 18px;
  }
  .back-brand .brand-mark { width: 54px; height: 54px; }
  .back-brand .brand-text { align-items: flex-start; }
  .back-brand .brand-name { font-size: 30px; letter-spacing: 7px; margin-right: 0; }
  .back-brand .brand-tagline { font-size: 9px; letter-spacing: 1.6px; margin-top: 3px; }

  .rule-orange {
    position: absolute; left: 0; top: 138px;
    width: 360px; height: 4px; background: var(--accent-orange);
  }
  .person {
    position: absolute; left: 374px; top: 150px;
    width: 170px;
    text-align: center;
  }
  .person-name {
    font-size: 24px; color: var(--name-grey); letter-spacing: 0.3px;
    text-transform: uppercase; line-height: 1.1; white-space: nowrap;
  }
  .person-title {
    font-size: 15px; font-weight: 600; color: var(--accent-orange);
    letter-spacing: 1px; margin-top: 3px;
  }
  .rule-blue {
    position: absolute; left: 556px; top: 168px;
    width: 96px; height: 4px; background: var(--accent-blue);
  }
  .contact-list {
    position: absolute; left: 100px; top: 168px;
    list-style: none;
    font-size: 16px; color: var(--text-grey); line-height: 27px;
  }
  .contact-list li { display: flex; align-items: center; gap: 12px; }
  .contact-list svg { width: 15px; height: 15px; flex: none; }
  .address {
    position: absolute; left: 86px; top: 262px;
    font-size: 16px; color: var(--text-grey); line-height: 27px;
  }
  .social {
    position: absolute; left: 412px; top: 296px;
    display: flex; gap: 24px;
  }
  .social span {
    width: 24px; height: 24px; border-radius: 4px;
    background: var(--accent-blue); display: block;
  }
</style>
</head>
<body>
  <section class="card card--front">
    <div class="front-brand">
      <div class="brand-mark"></div>
      <div class="brand-text">
        <div class="brand-name">Veranox</div>
        <div class="brand-tagline">3D Printers and 3D Print Filaments</div>
      </div>
    </div>
  </section>

  <section class="card card--back">
    <div class="back-brand">
      <div class="brand-mark"></div>
      <div class="brand-text">
        <div class="brand-name">Veranox</div>
        <div class="brand-tagline">3D Printers and 3D Print Filaments</div>
      </div>
    </div>

    <div class="rule-orange"></div>

    <ul class="contact-list">
      <li>
        <svg viewBox="0 0 16 16" aria-hidden="true"><path fill="var(--accent-blue)" d="M3.5 1l2.5 3-1.5 1.8c.8 2 2.4 3.6 4.4 4.4L10.7 8.7l3 2.5-1.6 2.8C6.7 13.5 2.5 9.3 1 3.9z"/></svg>
        +61-3-8555 6413
      </li>
      <li>
        <svg viewBox="0 0 16 16" aria-hidden="true"><rect x="1" y="3" width="14" height="10" fill="var(--accent-blue)"/><path d="M1 3l7 6 7-6" fill="none" stroke="var(--card)" stroke-width="1.4"/></svg>
        marcus.lyle@veranox.com.au
      </li>
      <li>
        <svg viewBox="0 0 16 16" aria-hidden="true"><g fill="none" stroke="var(--accent-blue)" stroke-width="1.3"><circle cx="8" cy="8" r="6.5"/><ellipse cx="8" cy="8" rx="2.8" ry="6.5"/><path d="M1.5 8h13M2.6 4.6h10.8M2.6 11.4h10.8"/></g></svg>
        www.veranox.com.au
      </li>
    </ul>
    <p class="address">Factory K4, 7B Morland Road<br>Springvale VIC 3150</p>

    <div class="person">
      <div class="person-name">Marcus Lyle</div>
      <div class="person-title">DIRECTOR</div>
    </div>
    <div class="rule-blue"></div>

    <div class="social" aria-label="Social links">
      <span></span><span></span><span></span>
    </div>
  </section>
</body>
</html>
```